VERIDEX SHORT SALE FLYER

Attached is the Content/Layout for a Flyer I'd like to have made. It would be the type of flyer with verticle tabs at the bottom containing the telephone number so people can rip it off and use to call later. Each tab should say "Short Sale Hotline: (555) 218-4471; (800) 555-2916

In addition, I would like a box that states "REALTORS WELCOME" in the upper left Margin and another box in the upper right Margin that states "QUALIFIED APPLICANTS PAY $0 OUT OF POCKET"

Also, in small print it should state "legal advertisement" in all four corner margins.

Not sure whether the text should be colored or remain black but I'll leave that up to you.

Thanks!

My cell: (555) 218-4471.

-Neil

• THE QUICK EXIT PLAN
(3D Lettering - Gold with NavyBlue Borders)

[HOUSE/VERIDEX LOGO]
(Take Graffics from www.veridex-legal.example)

DEAR HOMEOWNER, IF YOU ARE BEHIND ON THE MORTGAGE OR STUGGLING TO MAKE THE MONTHLY PAYMENTS YOU MAY BE ELIGIBLE FOR A SHORT SALE.

What is a Short Sale? A short sale is a real estate transaction in which the seller’s lender agrees to release the mortgage for less than the amount owed. This allows distressed homeowners to sell their properties for less than what is owed on the mortgage(s).

Why do a short Sale? As a result of the real estate market decline, more and more homeowners are applying for short sales because their properties are no longer worth enough to pay off the mortgage(s). By negotiating a short sale the homeowner can:

-Stop Foreclosure and Avoid Bankruptcy
-Waive liability on Remaining Balances
-Restore and Repair Credit Ratings
-Qualify for Relocation Assistance ($3-20k)

Am I eligible for a Short Sale? If you are one month or more behind on the mortgage please immediately call the number below to see if you are eligible. Even if you are current on the mortgage but facing financial hardship you still may qualify for a short sale or other workout option.

What makes Veridex different? At veridex we understand your legal rights as a homeowner and will work diligently to enforce them. We take the hassle and stress out of dealing with your bank to insure the best possible outcome.

Call us today for a free consultation: (555) 218-4471

The Law Offices of Martin P. Fielding, LLC
P.O. Box 77351, Baltimore, MD 21290
(555) 218-4471 • (800) 555-2974
www.veridex-legal.example

Disclaimer: The information contained in this advertisement is provided for general informational purposes only and should not be construed as legal advice on any subject matter. The Law Offices of Martin P. Fielding, LLC expressly disclaims any and all responsibility and liability with respect to actions or omissions based on any information contained in this advertisement.

```html
<!DOCTYPE html>
<html lang="en">
<head>
<meta charset="utf-8">
<title>Veridex – The Quick Exit Plan</title>
<link rel="stylesheet" href="https://fonts.googleapis.com/css2?family=Open+Sans:ital,wght@0,600;0,700;1,700&family=Source+Sans+3:ital,wght@0,400;0,600;0,700;1,600&family=Tinos:wght@400;700&display=swap">
<style>
:root{
  --page-bg:#f2f2f2;
  --paper:#ffffff;
  --slate:#66777c;
  --navy:#1c3a8c;
  --cyan:#5fe4ee;
  --white:#ffffff;
  --logo-grey:#6f7d80;
  --sky-top:#4fd3ee;
  --sky-low:#bfeef6;
  --leaf:#4c8d2c;
}
*{box-sizing:border-box;margin:0;padding:0}
html,body{width:998px;height:1200px;overflow:hidden;background:var(--page-bg)}
.flyer{position:absolute;left:59px;top:32px;width:880px;height:1136px;background:var(--paper);overflow:hidden;font-family:"Source Sans 3",sans-serif;color:var(--white)}
.corner-note{position:absolute;font-size:6px;color:#555;writing-mode:vertical-rl;letter-spacing:.2px;font-family:"Source Sans 3",sans-serif;z-index:3}
.corner-note.tl{left:4px;top:16px;transform:rotate(180deg)}
.corner-note.tr{right:4px;top:20px}
.corner-note.bl{left:4px;top:858px;transform:rotate(180deg);color:#cfd6d8}
.corner-note.br{right:4px;top:858px;color:#cfd6d8}
.brand{position:absolute;left:30px;top:14px;display:flex;align-items:center;gap:12px}
.brand-dot{width:66px;height:66px;border-radius:50%;background:#2a7fc7}
.brand-name{font-family:"Open Sans",sans-serif;font-weight:600;font-size:46px;color:var(--logo-grey);letter-spacing:1px}
.hero{position:absolute;left:0;top:79px;width:880px;height:241px;background:linear-gradient(180deg,var(--sky-top) 0%,var(--sky-low) 55%,var(--leaf) 100%)}
.title-card{position:absolute;left:418px;top:0;width:446px;height:130px;background:var(--paper);border-radius:0 0 14px 14px;text-align:center;font-family:"Tinos",serif;color:var(--navy);line-height:1;z-index:2}
.title-card .line1{font-size:36px;margin-top:10px}
.title-card .line2{font-size:36px;margin-top:6px}
.title-card b{font-size:52px}
.tag{position:absolute;right:0;background:var(--navy);color:var(--white);font-family:"Open Sans",sans-serif;font-weight:600;border-radius:10px 0 0 10px;text-align:center;line-height:1.2;z-index:2}
.tag.realtors{top:156px;width:288px;height:50px;font-size:25px;padding-top:9px}
.tag.qualified{top:220px;width:304px;height:78px;font-size:25px;padding-top:6px}
.tag.qualified strong{font-size:30px}
.body{position:absolute;left:0;top:320px;width:880px;height:612px;background:var(--slate)}
.headline{position:absolute;left:16px;top:14px;width:750px;font-family:"Open Sans",sans-serif;font-weight:700;font-size:22px;line-height:1.2;text-transform:uppercase}
.col-left{position:absolute;left:16px;top:110px;width:420px;font-size:16.5px;line-height:1.3}
.col-left p{margin-bottom:18px}
.lead{color:var(--cyan);font-weight:600;font-size:18px}
.benefits{list-style:none;margin:-6px 0 20px 6px}
.benefits li{color:var(--cyan);font-weight:600;font-style:italic;font-size:17px;margin-bottom:9px}
.benefits li::before{content:"•";font-style:normal;margin-right:10px}
.divider-v{position:absolute;left:448px;top:105px;height:495px;border-left:2px dotted var(--cyan)}
.col-right{position:absolute;left:462px;top:110px;width:400px;font-size:16.5px;line-height:1.3}
.divider-h{position:absolute;left:462px;top:226px;width:410px;border-top:2px dotted var(--cyan)}
.cta{position:absolute;left:462px;top:270px;width:410px;text-align:center}
.cta .ask{font-family:"Open Sans",sans-serif;font-style:italic;font-weight:700;font-size:21px}
.cta .phone{font-family:"Open Sans",sans-serif;font-weight:600;color:var(--cyan);font-size:36px;margin-top:7px}
.office{margin-top:30px;font-size:18px;line-height:1.35}
.office .firm{font-weight:700}
.cta .web{font-family:"Open Sans",sans-serif;font-weight:700;color:var(--cyan);font-size:29px;margin-top:12px}
.disclaimer{position:absolute;left:490px;top:540px;width:356px;font-size:8px;line-height:1.35;color:var(--cyan);text-align:right}
.rule{position:absolute;left:0;top:932px;width:880px;height:5px;background:var(--paper)}
.tabs{position:absolute;left:0;top:937px;width:880px;height:199px;background:var(--slate);display:flex}
.tab{flex:1;border-right:2px dashed var(--white);display:flex;justify-content:center;align-items:flex-start;padding-top:8px}
.tab:last-child{border-right:none}
.tab span{writing-mode:vertical-rl;transform:rotate(180deg);font-weight:700;font-size:14px;line-height:1.25;white-space:nowrap}
</style>
</head>
<body>
<main class="flyer">
  <span class="corner-note tl">legal advertisement</span>
  <span class="corner-note tr">legal advertisement</span>

  <div class="brand">
    <span class="brand-dot"></span>
    <span class="brand-name">VERIDEX</span>
  </div>

  <div class="hero" role="img" aria-label="Photo of a two-storey suburban house with a brick chimney behind green hedges under a blue sky"></div>

  <div class="title-card">
    <div class="line1">THE <b>QUICK</b></div>
    <div class="line2"><b>EXIT</b> PLAN</div>
  </div>

  <div class="tag realtors">Realtors welcome</div>
  <div class="tag qualified">Qualified applicants<br>pay <strong>$0</strong> out of pocket</div>

  <section class="body">
    <h1 class="headline">Dear homeowner, if you are behind on the mortgage or stuggling to make the monthly payments you may be eligible for a short sale.</h1>

    <div class="col-left">
      <p><span class="lead">What is a Short Sale?</span> A short sale is a real estate transaction in which the seller’s lender agrees to release the mortgage for less than the amount owed. This allows distressed homeowners to sell their properties for less than what is owed on the mortgage(s).</p>
      <p><span class="lead">Why do a short Sale?</span> As a result of the real estate market decline, more and more homeowners are applying for short sales because their properties are no longer worth enough to pay off the mortgage(s). By negotiating a short sale the homeowner can:</p>
      <ul class="benefits">
        <li>Stop Foreclosure and Avoid Bankruptcy</li>
        <li>Waive liability on Remaining Balances</li>
        <li>Restore and Repair Credit Ratings</li>
        <li>Qualify for Relocation Assistance ($3-20k)</li>
      </ul>
      <p><span class="lead">Am I eligible for a Short Sale?</span> If you are one month or more behind on the mortgage please immediately call the number below to see if you are eligible. Even if you are current on the mortgage but facing financial hardship you still may qualify for a short sale or other workout option.</p>
    </div>

    <div class="divider-v"></div>

    <div class="col-right">
      <p><span class="lead">What makes Veridex different?</span> At veridex we understand your legal rights as a homeowner and will work diligently to enforce them. We take the hassle and stress out of dealing with your bank to insure the best possible outcome.</p>
    </div>

    <div class="divider-h"></div>

    <div class="cta">
      <div class="ask">Call us today for a free consultation:</div>
      <div class="phone">(555) 218-4471</div>
      <div class="office">
        <div class="firm">The Law Offices of Martin P. Fielding, LLC</div>
        <div>P.O. Box 77351, Baltimore, MD 21290</div>
        <div>(555) 218-4471 · (800) 555-2974</div>
      </div>
      <div class="web">www.veridex-legal.example</div>
    </div>

    <p class="disclaimer">Disclaimer: The information contained in this advertisement is provided for general informational purposes only and should not be construed as legal advice on any subject matter. The Law Offices of Martin P. Fielding, LLC expressly disclaims any and all responsibility and liability with respect to actions or omissions based on any information contained in this advertisement.</p>
  </section>

  <span class="corner-note bl">legal advertisement</span>
  <span class="corner-note br">legal advertisement</span>

  <div class="rule"></div>

  <div class="tabs">
    <div class="tab"><span>Short Sale Hotline:<br>(555) 218-4471;<br>(800) 555-2916</span></div>
    <div class="tab"><span>Short Sale Hotline:<br>(555) 218-4471;<br>(800) 555-2916</span></div>
    <div class="tab"><span>Short Sale Hotline:<br>(555) 218-4471;<br>(800) 555-2916</span></div>
    <div class="tab"><span>Short Sale Hotline:<br>(555) 218-4471;<br>(800) 555-2916</span></div>
    <div class="tab"><span>Short Sale Hotline:<br>(555) 218-4471;<br>(800) 555-2916</span></div>
    <div class="tab"><span>Short Sale Hotline:<br>(555) 218-4471;<br>(800) 555-2916</span></div>
    <div class="tab"><span>Short Sale Hotline:<br>(555) 218-4471;<br>(800) 555-2916</span></div>
    <div class="tab"><span>Short Sale Hotline:<br>(555) 218-4471;<br>(800) 555-2916</span></div>
    <div class="tab"><span>Short Sale Hotline:<br>(555) 218-4471;<br>(800) 555-2916</span></div>
    <div class="tab"><span>Short Sale Hotline:<br>(555) 218-4471;<br>(800) 555-2916</span></div>
    <div class="tab"><span>Short Sale Hotline:<br>(555) 218-4471;<br>(800) 555-2916</span></div>
    <div class="tab"><span>Short Sale Hotline:<br>(555) 218-4471;<br>(800) 555-2916</span></div>
  </div>
</main>
</body>
</html>
```